Used Car Dealer seeks an Amazing Business Card Design

We are looking for a business card design that incorporates our logo and grabs the attention of anyone we give the business card to.

Looking to use the same colors as the logo. Our Logo choice is the black background with Red and Silver/Grey Lettering.

We also would like to see some embossed designs.

Target Market(s)

Used Car Buyers, Automotive, Auto

Industry/Entity Type

Automotive

Contact Information for Business Card

BVEX7K
Gordon Whitley
482 Tenbrook Lane
Suite 305
Roswell, GA 30098
Office (770) 555-0142
Cell (770) 555-0187
bvex7kga@mailnest.example
www.bvex7kga.example

Colors
ffffff
ee3036

Requirements
Must have
• Must include our logo (Black Background with Red and Silver/Grey Lettering)
Nice to have
• Embossed Design. Can be Single or Double Sided.

```html
<!DOCTYPE html>
<html lang="en">
<head>
<meta charset="utf-8">
<title>BVEX7K Business Card</title>
<link href="https://fonts.googleapis.com/css2?family=Open+Sans:wght@400;600&display=swap" rel="stylesheet">
<style>
  :root {
    --backdrop: #a7a6ab;
    --card-dark: #151515;
    --card-mid: #3a3a3a;
    --accent-red: #ee3036;
    --text-white: #ffffff;
    --text-silver: #d8d8d8;
  }
  * { margin: 0; padding: 0; box-sizing: border-box; }
  html, body {
    width: 1200px; height: 863px; overflow: hidden;
    background: var(--backdrop);
    font-family: "Open Sans", sans-serif;
  }
  .canvas { position: relative; width: 1200px; height: 863px; }
  .card {
    position: absolute; left: 285px; width: 630px; height: 360px;
    background: linear-gradient(135deg, var(--card-dark) 0%, #242424 45%, var(--card-mid) 100%);
    overflow: hidden;
    box-shadow: 0 10px 24px rgba(0,0,0,0.35);
  }
  .card--front { top: 46px; }
  .card--back { top: 456px; }
  .accent-bar { position: absolute; width: 7px; background: var(--accent-red); }
  .accent-bar--left { left: 0; top: 0; height: 130px; }
  .accent-bar--right { right: 0; bottom: 0; height: 150px; }
  .brand {
    position: absolute; display: flex; align-items: center; gap: 14px;
    font-weight: 600; color: var(--text-silver); letter-spacing: 2px;
  }
  .brand__dot { width: 22px; height: 22px; border-radius: 50%; background: var(--accent-red); }
  .card--front .brand { left: 50%; top: 50%; transform: translate(-50%, -60%); font-size: 64px; }
  .website {
    position: absolute; left: 40px; bottom: 34px;
    color: var(--accent-red); font-size: 13px; letter-spacing: 0.5px;
  }
  .card--back .brand { left: 300px; top: 62px; font-size: 50px; }
  .owner {
    position: absolute; right: 402px; top: 200px; text-align: right; color: var(--text-white);
  }
  .owner__name { font-size: 21px; }
  .owner__title { font-size: 13px; margin-top: 2px; color: var(--text-silver); }
  .divider {
    position: absolute; left: 238px; top: 198px; width: 2px; height: 96px; background: var(--accent-red);
  }
  .contact-list { position: absolute; left: 252px; top: 202px; list-style: none; }
  .contact-list li {
    display: flex; align-items: center; gap: 8px;
    color: var(--text-white); font-size: 13px; line-height: 1; margin-bottom: 9px;
  }
  .contact-icon { width: 15px; height: 15px; flex: none; }
</style>
</head>
<body>
<main class="canvas">
  <section class="card card--front" aria-label="Card front">
    <span class="accent-bar accent-bar--left"></span>
    <span class="accent-bar accent-bar--right"></span>
    <div class="brand"><span class="brand__dot"></span>BVEX7K</div>
    <p class="website">www.bvex7kga.example</p>
  </section>

  <section class="card card--back" aria-label="Card back">
    <span class="accent-bar accent-bar--left"></span>
    <span class="accent-bar accent-bar--right"></span>
    <div class="brand"><span class="brand__dot"></span>BVEX7K</div>
    <div class="owner">
      <p class="owner__name">Gordon Whitley</p>
      <p class="owner__title">Owner</p>
    </div>
    <span class="divider"></span>
    <ul class="contact-list">
      <li>
        <svg class="contact-icon" viewBox="0 0 16 16"><circle cx="8" cy="8" r="8" fill="#ee3036"/><path d="M8 3.5a3 3 0 0 0-3 3c0 2.2 3 5.5 3 5.5s3-3.3 3-5.5a3 3 0 0 0-3-3z" fill="#fff"/><circle cx="8" cy="6.5" r="1.1" fill="#ee3036"/></svg>
        482 Tenbrook Lane, Suite 305, Roswell, GA 30098
      </li>
      <li>
        <svg class="contact-icon" viewBox="0 0 16 16"><circle cx="8" cy="8" r="8" fill="#ee3036"/><rect x="4" y="5" width="8" height="6" fill="#fff"/><path d="M4 5l4 3.2L12 5" stroke="#ee3036" stroke-width="0.9" fill="none"/></svg>
        bvex7kga@mailnest.example
      </li>
      <li>
        <svg class="contact-icon" viewBox="0 0 16 16"><circle cx="8" cy="8" r="8" fill="#ee3036"/><path d="M5.5 4l1.6 2.2-0.9 1c.5 1 1.3 1.8 2.3 2.3l1-.9 2.2 1.6-.8 1.3C8.2 11.5 4.5 7.8 4.2 4.8z" fill="#fff"/></svg>
        (770) 555-0142
      </li>
      <li>
        <svg class="contact-icon" viewBox="0 0 16 16"><circle cx="8" cy="8" r="8" fill="#ee3036"/><path d="M5.5 4l1.6 2.2-0.9 1c.5 1 1.3 1.8 2.3 2.3l1-.9 2.2 1.6-.8 1.3C8.2 11.5 4.5 7.8 4.2 4.8z" fill="#fff"/></svg>
        (770) 555-0187
      </li>
    </ul>
  </section>
</main>
</body>
</html>
```